New Customers - Women's Apparel Postcard

We are in the process of buying a mailing list to try to get some new customers. We would like to entice them with a bunch of pictures of our clothing and a lucrative offer. I will attach some examples.
MAIN MESSAGE: We have great fashion for women of all ages & all sizes!
SECONDARY MESSAGE: Try us on, you are gonna love our great fashions:
OFFER: $10.00 off $20.00 purchase

Target Market(s)

45+ women

Industry/Entity Type

Womens Clothing

Requirements
Must have
• strong call to action

```html
<!DOCTYPE html>
<html lang="en">
<head>
<meta charset="utf-8">
<title>Lark &amp; Linen – New Customer Postcard</title>
<link href="https://fonts.googleapis.com/css2?family=Didact+Gothic&family=Poppins:wght@500;600&family=Marcellus&family=Playfair+Display:ital@1&display=swap" rel="stylesheet">
<style>
  :root {
    --stage: #3a3a3a;
    --paper: #ffffff;
    --ink: #111111;
    --rule: #9a9a9a;
    --pale-yellow: #fbd97e;
    --gold: #ecb84a;
    --orange: #f7941d;
    --maroon: #962a2b;
    --red: #ec2328;
    --pink: #ec168c;
    --photo-light: #ece9e6;
    --photo-mid: #8a4a45;
    --photo-dark: #4a3f3c;
  }
  * { box-sizing: border-box; margin: 0; padding: 0; }
  html, body { width: 1200px; height: 1000px; overflow: hidden; }
  body { background: var(--stage); position: relative; font-family: "Didact Gothic", sans-serif; color: var(--ink); }

  .card { position: absolute; background: var(--paper); transform-origin: top left; }
  .card-front { left: 280px; top: 26px; width: 575px; height: 420px; transform: scale(1.113); }
  .card-back { left: 260px; top: 512px; width: 629px; height: 428px; transform: scale(1.08); }

  .abs { position: absolute; }

  /* swatch strips */
  .swatch-column { display: grid; grid-template-columns: repeat(2, 1fr); grid-auto-flow: column; grid-template-rows: repeat(6, 1fr); gap: 2px; }
  .swatch-row { display: grid; grid-template-columns: repeat(6, 1fr); gap: 2px; }
  .sw-py { background: var(--pale-yellow); }
  .sw-go { background: var(--gold); }
  .sw-or { background: var(--orange); }
  .sw-ma { background: var(--maroon); }
  .sw-re { background: var(--red); }
  .sw-pi { background: var(--pink); }

  /* front */
  .model-photo { left: 28px; top: 8px; width: 240px; height: 226px;
    background: linear-gradient(90deg, var(--paper) 0%, var(--photo-dark) 22%, var(--photo-light) 48%, var(--photo-mid) 68%, var(--photo-dark) 80%, var(--paper) 100%); }
  .headline { left: 262px; top: 20px; width: 310px; text-align: center; font-family: "Poppins", sans-serif; font-weight: 600; font-size: 15px; line-height: 20px; }
  .pitch-box { left: 260px; top: 70px; width: 282px; height: 160px; border: 2px solid var(--ink); border-radius: 18px; padding: 10px 0 0 24px; font-size: 28px; line-height: 35px; }
  .pitch-box .accent { font-family: "Poppins", sans-serif; font-weight: 500; letter-spacing: 4px; font-size: 27px; }
  .pitch-swatches { left: 522px; top: 80px; width: 52px; height: 138px; }

  .offer-box { left: 36px; top: 238px; width: 276px; height: 162px; background: var(--ink); border-radius: 14px; color: var(--paper); text-align: center; overflow: hidden; }
  .offer-title { position: absolute; left: 0; right: 0; top: 10px; font-family: "Marcellus", serif; font-weight: 400; font-size: 56px; letter-spacing: 1px; }
  .offer-rule { position: absolute; left: 20px; right: 0; top: 83px; height: 1px; background: var(--rule); }
  .offer-terms { position: absolute; left: 0; right: 0; top: 92px; font-family: "Playfair Display", serif; font-style: italic; font-size: 20px; line-height: 30px; }
  .offer-swatches { left: 24px; top: 250px; width: 30px; height: 140px; }

  .brand-box { left: 320px; top: 238px; width: 220px; height: 162px; border: 2px solid var(--ink); border-radius: 14px; }
  .brand-name { font-family: "Poppins", sans-serif; font-weight: 600; color: var(--ink); white-space: nowrap; }
  .brand-box .brand-name { position: absolute; left: 16px; top: 96px; font-size: 20px; }
  .brand-box .brand-url { position: absolute; left: 16px; top: 140px; font-family: "Poppins", sans-serif; font-size: 7.5px; font-weight: 500; }
  .brand-swatches { left: 478px; top: 306px; width: 34px; height: 88px; }

  /* back */
  .top-strip { left: 190px; top: 0; width: 236px; height: 30px; }
  .bottom-strip { left: 190px; top: 398px; width: 236px; height: 30px; }
  .return-address { left: 180px; top: 42px; width: 256px; text-align: center; font-size: 17px; line-height: 21px; }
  .stamp-box { left: 493px; top: 45px; width: 116px; height: 89px; border: 2px solid var(--ink); }
  .card-back .brand-name { position: absolute; left: 44px; top: 248px; font-size: 38px; }
  .card-back .brand-url { position: absolute; left: 52px; top: 338px; font-family: "Poppins", sans-serif; font-size: 13px; font-weight: 500; letter-spacing: 0.3px; }
  .divider { left: 309px; top: 135px; width: 2px; height: 222px; background: var(--ink); }
  .address-line { left: 330px; width: 292px; height: 2px; background: var(--ink); }
</style>
</head>
<body>

<section class="card card-front" aria-label="Postcard front">
  <div class="abs model-photo" role="img" aria-label="Photo of two women modelling the store's knit vest and red patterned wrap"></div>

  <p class="abs headline">We have great fashion for<br>women of all ages &amp; all sizes!</p>

  <div class="abs pitch-box">
    <p>Try us on................</p>
    <p>You Are Gonna</p>
    <p>Love Our Great</p>
    <p class="accent">Fashions!</p>
  </div>
  <div class="abs swatch-column pitch-swatches">
    <span class="sw-py"></span><span class="sw-go"></span><span class="sw-or"></span><span class="sw-ma"></span><span class="sw-re"></span><span class="sw-pi"></span>
    <span class="sw-pi"></span><span class="sw-re"></span><span class="sw-ma"></span><span class="sw-or"></span><span class="sw-go"></span><span class="sw-py"></span>
  </div>

  <div class="abs offer-box">
    <h2 class="offer-title">OFFER</h2>
    <div class="offer-rule"></div>
    <p class="offer-terms">$10.00 off $20.00<br>purchase</p>
  </div>
  <div class="abs swatch-column offer-swatches">
    <span class="sw-pi"></span><span class="sw-go"></span><span class="sw-or"></span><span class="sw-ma"></span><span class="sw-re"></span><span class="sw-pi"></span>
    <span class="sw-pi"></span><span class="sw-re"></span><span class="sw-ma"></span><span class="sw-or"></span><span class="sw-go"></span><span class="sw-py"></span>
  </div>

  <div class="abs brand-box">
    <span class="brand-name">Lark &amp; Linen</span>
    <span class="brand-url">www.larklinenstyle.com</span>
  </div>
  <div class="abs swatch-column brand-swatches">
    <span class="sw-py"></span><span class="sw-go"></span><span class="sw-or"></span><span class="sw-ma"></span><span class="sw-re"></span><span class="sw-pi"></span>
    <span class="sw-pi"></span><span class="sw-re"></span><span class="sw-ma"></span><span class="sw-or"></span><span class="sw-go"></span><span class="sw-py"></span>
  </div>
</section>

<section class="card card-back" aria-label="Postcard back">
  <div class="abs swatch-row top-strip">
    <span class="sw-py"></span><span class="sw-go"></span><span class="sw-or"></span><span class="sw-ma"></span><span class="sw-re"></span><span class="sw-pi"></span>
  </div>
  <p class="abs return-address">214 North Elm Street<br>Hartwell, IL 61990</p>
  <div class="abs stamp-box" aria-label="Stamp area"></div>

  <span class="brand-name">Lark &amp; Linen</span>
  <span class="brand-url">www.larklinenstyle.com</span>

  <div class="abs divider"></div>
  <div class="abs address-line" style="top:221px"></div>
  <div class="abs address-line" style="top:249px"></div>
  <div class="abs address-line" style="top:277px"></div>

  <div class="abs swatch-row bottom-strip">
    <span class="sw-pi"></span><span class="sw-re"></span><span class="sw-ma"></span><span class="sw-or"></span><span class="sw-go"></span><span class="sw-py"></span>
  </div>
</section>

</body>
</html>
```